5 post cards for B2B Advertising

We are an electrical lighting contractor advertising our Lighting and Electrical services to property management companies, car dealer ships, hotels, schools, malls, and shopping centers.

RED / White / Blue themed American flag.

Post Cards

1. Electrical Services
2. Lighting Services and conversions to LED
3. Sign Repairs and conversions to LED
4. Nighttime Lighting Inspections (report lights and signs out)
5. Lighting is Safety

```html
<!DOCTYPE html>
<html lang="en">
<head>
<meta charset="utf-8">
<title>Nighttime Lighting Inspections – Beacon Upkeep Inc</title>
<link rel="stylesheet" href="https://fonts.googleapis.com/css2?family=Orbitron:wght@600;700&family=Encode+Sans+Semi+Condensed:wght@400;500;800&display=swap">
<style>
  :root {
    --red: #e30613;
    --navy: #2e2d80;
    --white: #ffffff;
    --night-deep: #153e63;
    --night-light: #2a6496;
    --display: "Orbitron", sans-serif;
    --text: "Encode Sans Semi Condensed", sans-serif;
  }
  * { margin: 0; padding: 0; box-sizing: border-box; }
  html, body { width: 1200px; height: 776px; overflow: hidden; background: var(--white); }
  .postcard { position: relative; width: 1200px; height: 776px; overflow: hidden; background: var(--white); font-family: var(--text); }

  .backdrop { position: absolute; inset: 0; }

  .headline-top {
    position: absolute; left: 118px; top: 34px;
    font-family: var(--display); font-weight: 700; font-size: 43px;
    color: var(--red); letter-spacing: 1px; white-space: nowrap;
  }
  .headline-pill {
    position: absolute; left: 181px; top: 88px; width: 377px; height: 71px;
    background: var(--navy); border-radius: 36px;
    display: flex; align-items: center; justify-content: center;
    font-family: var(--display); font-weight: 700; font-size: 40px;
    color: var(--white); letter-spacing: 1px;
  }
  .intro, .details {
    position: absolute; left: 37px;
    font-size: 23.5px; line-height: 30.5px; color: var(--navy); font-weight: 400;
  }
  .intro { top: 177px; width: 560px; }
  .details { top: 375px; width: 500px; }

  .tag {
    position: absolute; left: 37px; height: 60px;
    border-radius: 30px; display: flex; align-items: center;
    font-family: var(--display); font-weight: 700; font-size: 25px; color: var(--white);
    padding-left: 76px; letter-spacing: 1px;
  }
  .tag::before {
    content: ""; position: absolute; left: 0; top: -4px;
    width: 68px; height: 68px; border-radius: 50%;
    background: var(--white); border: 3px solid currentColor;
  }
  .tag-services { top: 292px; width: 316px; background: var(--navy); }
  .tag-services::before { border-color: var(--navy); }
  .tag-schedule { top: 522px; width: 333px; background: var(--red); }
  .tag-schedule::before { border-color: var(--red); }

  .contact {
    position: absolute; left: 0; top: 620px; width: 610px;
    display: flex; flex-direction: column; align-items: center; gap: 11px;
  }
  .contact-line {
    display: flex; align-items: center; gap: 9px;
    color: var(--white); font-size: 24px; font-weight: 500; line-height: 33px;
  }
  .contact-line svg { width: 33px; height: 33px; flex: none; }

  .brand {
    position: absolute; left: 760px; top: 38px; width: 410px;
    text-align: center; color: var(--red); font-family: var(--text); font-weight: 800;
    line-height: 1;
  }
  .brand-name { display: block; font-size: 74px; letter-spacing: 1px; }
  .brand-sub { display: block; font-size: 27px; margin-top: 8px; letter-spacing: 1px; }
</style>
</head>
<body>
<main class="postcard">
  <svg class="backdrop" width="1200" height="776" viewBox="0 0 1200 776" aria-hidden="false">
    <defs>
      <linearGradient id="night-sky" x1="0" y1="0" x2="0.4" y2="1">
        <stop offset="0" stop-color="var(--night-deep)"/>
        <stop offset="1" stop-color="var(--night-light)"/>
      </linearGradient>
    </defs>
    <path class="contact-band" d="M0 776 L0 700 Q10 610 110 608 L560 608 L560 776 Z" fill="var(--navy)"/>
    <circle class="photo-area" cx="968" cy="682" r="452" fill="url(#night-sky)" role="img"
      aria-label="Photo at night: technician in a bucket lift servicing a square parking-lot light fixture on a pole"/>
  </svg>

  <h1 class="headline-top">NIGHTTIME LIGHTING</h1>
  <div class="headline-pill">INSPECTIONS</div>

  <p class="intro">Beacon Upkeep Inc (BUI) provides Night Inspection services for Shopping Centers and Malls! Free of charge if you sign up for our service agreement.</p>

  <div class="tag tag-services">OUR SERVICES</div>

  <p class="details">We'll inspect your property at night documenting any pole, canopy, or security lights that are out. We also provide photographs of any signs that are in need of repair.</p>

  <div class="tag tag-schedule">SCHEDULE NOW</div>

  <div class="contact">
    <div class="contact-line">
      <svg viewBox="0 0 34 34" fill="none" stroke="currentColor" stroke-width="2"><circle cx="17" cy="17" r="15.5"/><path d="M11 9.5l3 -0.5 2 4.5 -2 1.5c1 2.5 3 4.5 5 5.5l1.5-2 4.5 2 -0.5 3c-1 1-3 1.2-5 0.3-4-1.8-7.5-5.3-9-9.5-0.6-2 -0.3-3.8 0.5-4.8z" fill="currentColor" stroke="none"/></svg>
      <span>877-555-0148</span>
    </div>
    <div class="contact-line">
      <svg viewBox="0 0 34 34" fill="none" stroke="currentColor" stroke-width="1.8"><circle cx="17" cy="17" r="15.5"/><ellipse cx="17" cy="17" rx="7" ry="15.5"/><line x1="17" y1="1.5" x2="17" y2="32.5"/><line x1="1.5" y1="17" x2="32.5" y2="17"/><path d="M4 9h26M4 25h26"/></svg>
      <span>BeaconUpkeep.com</span>
    </div>
    <div class="contact-line">
      <svg viewBox="0 0 34 34" fill="none" stroke="currentColor" stroke-width="2"><circle cx="17" cy="17" r="15.5"/><rect x="9" y="11.5" width="16" height="11" rx="1.5"/><path d="M9.5 12.5l7.5 6 7.5-6"/></svg>
      <span>Service@BeaconUpkeep.com</span>
    </div>
  </div>

  <div class="brand">
    <span class="brand-name">BEACON</span>
    <span class="brand-name">UPKEEP</span>
    <span class="brand-sub">INCORPORATED</span>
  </div>
</main>
</body>
</html>
```